Orthopedic Landing Page Website Design

We are working with a Orthopedic Medical Group in California. They provide orthopedic services throughout California.

Some sites to use for inspiration:
https://www.kvreth.com
https://belvantrix.com
https://www.quellbridgevex.com
https://tarnwickfelvaspring.com

Thank you for taking the time to consider designing a website for us. We are web developers based in Stockton, CA, USA. Most of our projects go through the same process. Understanding this process may help you win a project with us. We custom-code all of our websites in-house. We don’t have any requirements as to what tools you use for your design, but we ask that you follow these guidelines.

IMAGES:
If you use any images or icons in the design, we ask that you have a link to the asset so we can purchase the image/icon. Most of the designs we submit do not have the customer’s images on them unless they have some great images. Be creative; show us the feeling you are trying to portray with your image choices. Use any royalty-free site you choose. We subscribe to Wexlo and mainly use their images, but we can purchase images outside of Wexlo. PLEASE NOTE: we will not submit designs to clients with watermarks on the images.

FONTS:
We ask that you identify the fonts you’re using in the design. This can be done in a message if you want. We typically use Pelmira Fonts and Wexlo Fonts.

CONTENT:
We're always open to different content and ideas. We often submit designs with stock images so the client can see our vision. We typically take pictures after the website launch to use their images with our vision. Lorem Ipsum is fine for paragraphs, but we ask that you make the Headers with correct English. We want to be able to show the vision and identify the sections of the website.

INSPIRATION:
We typically add a couple of links in the brief of websites we like to help you get started in your design.

REVISIONS:
We do not often ask for revisions of the designs unless we see something in the design that may not appeal to the client. If there are slight changes that we want to make, we do that in the development process.

FEEDBACK:
We rarely give feedback on designs during the design process. We are working on many website projects and do not have the time to provide feedback. We usually respond if your request is well thought out and asks specific questions, but a note asking “feedback, please” usually goes unanswered.

```html
<!DOCTYPE html>
<html lang="en">
<head>
<meta charset="utf-8">
<title>Kestra Orthopedic — Orthopedic Medical Group in California</title>
<link href="https://fonts.googleapis.com/css2?family=Playfair+Display:wght@400;500&family=Poppins:wght@400;500;600;700&display=swap" rel="stylesheet">
<style>
:root{
  --blue:#2a78b3;
  --red:#d5364f;
  --red-dark:#c22c45;
  --ink:#222;
  --text:#555;
  --muted:#888;
  --line:#e3e3e3;
  --grey-bg:#f1f1f1;
  --dark:#343434;
  --white:#fff;
}
*{box-sizing:border-box;margin:0;padding:0}
html,body{width:1200px;height:5396px;overflow:hidden}
body{font-family:"Poppins",sans-serif;color:var(--text);background:var(--white);position:relative}
.serif{font-family:"Playfair Display",serif;font-weight:400;text-transform:uppercase;color:var(--ink)}
.abs{position:absolute}
.btn{display:inline-flex;align-items:center;justify-content:center;font-weight:600;font-size:11px;text-transform:uppercase;letter-spacing:.3px;border-radius:3px;color:var(--white)}
.btn-blue{background:var(--blue)}
.btn-red{background:var(--red)}
.section-title{position:absolute;left:0;width:1200px;text-align:center;font-size:34px}
.section-title::after{content:"";display:block;width:50px;height:2px;background:#d8d8d8;margin:16px auto 0}
.ph{position:absolute}

/* header */
.logo{position:absolute;left:88px;top:20px}
.logo-name{font-family:"Poppins",sans-serif;font-weight:400;font-size:44px;letter-spacing:8px;color:var(--blue);line-height:1}
.logo-sub{font-family:"Playfair Display",serif;font-size:10px;letter-spacing:1.5px;color:var(--blue);margin-top:2px}
.call{position:absolute;left:615px;top:28px;display:flex;align-items:center;gap:10px}
.call-icon{width:38px;height:38px;border-radius:50%;background:#c9c9c9;display:flex;align-items:center;justify-content:center}
.call small{display:block;font-size:9px;color:var(--muted);text-transform:uppercase}
.call b{font-size:16px;color:var(--ink);font-weight:600}
.top-btn{position:absolute;top:28px;height:40px}
.nav{position:absolute;top:95px;left:0;width:1200px;height:45px;border-top:1px solid var(--line);border-bottom:1px solid var(--line);display:flex;align-items:center;padding-left:88px;gap:30px;font-size:12px;font-weight:500;color:#333;text-transform:uppercase}
.nav .search{position:absolute;right:88px}

/* hero */
.hero{position:absolute;top:140px;left:0;width:1200px;height:665px;background:linear-gradient(90deg,#f6f6f6 0%,#f0f0f0 45%,#e4e4e4 100%)}
.hero-photo{left:470px;top:0;width:730px;height:665px;background:linear-gradient(90deg,rgba(240,240,240,0) 0%,rgba(222,222,222,.85) 22%,#cfd1d3 45%,#a9bfcb 75%,#6f9bb5 100%)}
.hero-title{position:absolute;left:86px;top:172px;font-size:62px;line-height:66px}
.hero-sub{position:absolute;left:88px;top:325px;font-size:19px}
.hero-text{position:absolute;left:88px;top:370px;width:400px;font-size:14px;line-height:22px;color:#444}

/* specialties */
.specialties{position:absolute;top:805px;left:0;width:1200px;height:495px;background:linear-gradient(90deg,#c8283f 0%,#d5364f 55%,#d84358 100%)}
.specialties .section-title::after{background:rgba(255,255,255,.6)}
.spec-btn{position:absolute;width:256px;height:64px;background:var(--white);border-radius:3px;display:flex;align-items:center;justify-content:center;font-size:12px;font-weight:600;color:#222;text-transform:uppercase;box-shadow:0 3px 8px rgba(0,0,0,.12)}

/* about */
.about-text{position:absolute;left:630px;width:385px;font-size:13.5px;line-height:22px;color:#555}

/* journey */
.journey-card{position:absolute;top:2021px;width:249px;height:301px;border-radius:2px;overflow:hidden}
.journey-card span{position:absolute;left:32px;bottom:28px;color:var(--white);font-weight:700;font-size:14px;line-height:19px;text-transform:uppercase}
.arrow{position:absolute;top:2363px;width:52px;height:52px;border-radius:50%;display:flex;align-items:center;justify-content:center}

/* booking */
.form-box{position:absolute;left:88px;top:2661px;width:383px;height:411px;background:var(--blue);border-radius:3px;padding:30px}
.field label{display:block;font-size:10px;font-weight:600;color:var(--white);text-transform:uppercase;margin-bottom:8px}
.field div{background:rgba(255,255,255,.14);height:40px;border-radius:2px;font-size:11px;color:#cfe0ee;padding:12px 18px}

/* education */
.edu{position:absolute;top:3258px;width:300px;text-align:center}
.edu-circle{width:146px;height:146px;border-radius:50%;margin:0 auto;display:flex;align-items:center;justify-content:center}
.edu b{display:block;margin-top:32px;font-size:17px;font-weight:600;color:#222;text-transform:uppercase}
.edu small{display:block;margin-top:4px;font-size:13px;color:#666;text-transform:uppercase}
.edu-divider{position:absolute;top:3260px;width:1px;height:190px;background:var(--line)}

/* testimonials */
.review{position:absolute;top:3654px;width:446px;height:205px;background:var(--white);box-shadow:0 4px 18px rgba(0,0,0,.09);border-radius:3px}
.quote{position:absolute;left:26px;top:34px;width:88px;height:88px;border-radius:50%;background:#9a9a9a;color:var(--white);font-family:"Playfair Display",serif;font-size:84px;line-height:124px;text-align:center}
.review p{position:absolute;left:140px;top:38px;width:270px;font-size:12px;line-height:20px;color:#666}
.reviewer{position:absolute;left:140px;top:152px;display:flex;align-items:center;gap:10px}
.avatar{width:32px;height:32px;border-radius:50%;background:#b8b8b8}
.reviewer b{display:block;font-size:13px;color:#222;font-weight:600}
.reviewer small{font-size:11px;color:var(--muted)}
.stars{position:absolute;left:326px;top:160px;color:#f3a712;font-size:16px;letter-spacing:1px}

/* blog */
.blog-date{font-size:11px;color:var(--muted);text-transform:uppercase}
.blog-title{font-size:13px;font-weight:600;color:#222;text-transform:uppercase;line-height:18px}
.read-more{font-size:10px;font-weight:700;color:var(--red);text-transform:uppercase;text-decoration:underline}
.small-post{position:absolute;left:687px;width:174px;height:161px;border-radius:3px}
.small-meta{position:absolute;left:888px;width:200px}

/* cta & footer */
.footer{position:absolute;top:4879px;left:0;width:1200px;height:517px;background:var(--dark)}
.cta{position:absolute;left:165px;top:4766px;width:869px;height:186px;background:linear-gradient(90deg,#c9293f,#d73e56);border-radius:4px}
.foot-title{position:absolute;font-family:"Playfair Display",serif;text-transform:uppercase;color:var(--white);font-size:17px}
.foot-list{position:absolute;font-size:12px;line-height:26px;color:#ddd}
.social{width:34px;height:34px;border-radius:50%;background:#4a4a4a;display:inline-block;margin-right:10px}
</style>
</head>
<body>

<header>
  <div class="logo">
    <div class="logo-name">KESTRA</div>
    <div class="logo-sub">KESTRA ORTHOPEDIC</div>
  </div>
  <div class="call">
    <div class="call-icon"><svg width="18" height="18" viewBox="0 0 24 24"><path fill="#fff" d="M6.6 10.8a15.1 15.1 0 006.6 6.6l2.2-2.2c.3-.3.7-.4 1-.2 1.1.4 2.3.6 3.6.6.6 0 1 .4 1 1V20c0 .6-.4 1-1 1A17 17 0 013 4c0-.6.4-1 1-1h3.5c.6 0 1 .4 1 1 0 1.3.2 2.5.6 3.6.1.3 0 .7-.2 1z"/></svg></div>
    <div><small>Call us</small><b>(555) 214-0876</b></div>
  </div>
  <div class="btn btn-blue top-btn" style="left:816px;width:143px">Appointment</div>
  <div class="btn btn-red top-btn" style="left:968px;width:143px">Pay my bill</div>
  <nav class="nav">
    <svg width="16" height="14" viewBox="0 0 24 22"><path fill="#d5364f" d="M12 1L1 11h3v10h6v-6h4v6h6V11h3z"/></svg>
    <span>About us</span><span>Services</span><span>Our doctors</span><span>Conditions &amp; treatment</span><span>Patient info</span><span>Blog</span><span>Contact us</span>
    <svg class="search" width="15" height="15" viewBox="0 0 24 24"><circle cx="10" cy="10" r="7" fill="none" stroke="#333" stroke-width="2.5"/><path d="M15 15l7 7" stroke="#333" stroke-width="2.5"/></svg>
  </nav>
</header>

<section class="hero">
  <div class="ph hero-photo" role="img" aria-label="Physiotherapist guiding a woman stretching on an exercise ball"></div>
  <h1 class="serif hero-title">Orthopedic<br>Medical</h1>
  <div class="serif hero-sub">Group in California</div>
  <p class="hero-text">Discover how incredible you can feel naturally with focused, gentle and effective chiropractic care.</p>
  <div class="btn btn-blue abs" style="left:88px;top:440px;width:126px;height:38px">Learn more</div>
</section>

<section class="specialties">
  <h2 class="section-title serif" style="top:95px;color:#fff">Our Specialties</h2>
  <div class="spec-btn" style="left:203px;top:185px">Joint replacement</div>
  <div class="spec-btn" style="left:473px;top:185px">Hand &amp; wrist</div>
  <div class="spec-btn" style="left:741px;top:185px">Foot &amp; ankle</div>
  <div class="spec-btn" style="left:203px;top:265px">Spine</div>
  <div class="spec-btn" style="left:473px;top:265px">Sports medicine</div>
  <div class="spec-btn" style="left:741px;top:265px">Intervention pain</div>
  <div class="abs" style="left:0;width:1200px;top:377px;text-align:center;font-size:11px;font-weight:700;color:#fff;text-decoration:underline;text-transform:uppercase">View all services</div>
</section>

<section>
  <div class="ph" role="img" aria-label="Doctor examining a patient's shoulder" style="left:157px;top:1361px;width:420px;height:510px;border-radius:0 0 210px 210px;background:linear-gradient(180deg,#ffffff 0%,#eef1f3 35%,#c9cdd1 65%,#8a5a64 100%)"></div>
  <div class="abs" style="left:472px;top:1763px;width:96px;height:96px;border-radius:50%;background:#a9a9a9;display:flex;align-items:center;justify-content:center">
    <svg width="22" height="24" viewBox="0 0 22 24"><path d="M2 1l19 11L2 23z" fill="#fff"/></svg>
  </div>
  <h2 class="serif abs" style="left:630px;top:1392px;font-size:34px;line-height:40px">About Kestra<br>Orthopedic</h2>
  <p class="about-text" style="top:1500px">Orthopedic medicine, often referred to simply as orthopedics, is a branch of medicine that focuses on the diagnosis, treatment, and prevention of conditions and injuries related to the musculoskeletal system. This system includes bones, joints, ligaments, tendons, muscles, and other connective tissues</p>
  <p class="about-text" style="top:1670px">Orthopedic medical practitioners, known as orthopedic surgeons or orthopedists, are specially trained to treat a wide range of musculoskeletal issues.</p>
  <div class="btn btn-blue abs" style="left:631px;top:1784px;width:126px;height:38px">Learn more</div>
</section>

<section>
  <h2 class="section-title serif" style="top:1932px">Patient Journey</h2>
  <div class="journey-card" role="img" aria-label="Doctors reviewing a patient chart" style="left:88px;background:linear-gradient(180deg,#dfe5ea,#8a9aa8 70%,#4a5866)"><span>Our<br>consultation</span></div>
  <div class="journey-card" role="img" aria-label="Smiling doctor with a spine model" style="left:348px;background:linear-gradient(180deg,#e6e9ec,#9aa6b0 70%,#4e5a64)"><span>Understanding<br>options</span></div>
  <div class="journey-card" role="img" aria-label="Doctor treating a patient's leg" style="left:605px;background:linear-gradient(180deg,#d6dbe0,#8c97a0 70%,#4a545c)"><span>Treatment<br>plan</span></div>
  <div class="journey-card" role="img" aria-label="Surgeons operating" style="left:863px;background:linear-gradient(180deg,#a9c7dd,#5d88a8 70%,#2f4c63)"><span>Orthopedic<br>surgery</span></div>
  <div class="arrow" style="left:545px;background:var(--blue)"><svg width="10" height="12" viewBox="0 0 10 12"><path d="M7 1L2 6l5 5" stroke="#fff" stroke-width="2" fill="none"/></svg></div>
  <div class="arrow" style="left:603px;background:var(--red)"><svg width="10" height="12" viewBox="0 0 10 12"><path d="M3 1l5 5-5 5" stroke="#fff" stroke-width="2" fill="none"/></svg></div>
</section>

<section>
  <div class="abs" style="left:0;top:2502px;width:1200px;height:524px;background:var(--grey-bg)"></div>
  <div class="ph" role="img" aria-label="Therapist examining a patient's lower back" style="left:482px;top:2502px;width:718px;height:524px;background:linear-gradient(90deg,rgba(241,241,241,0) 0%,#dcdcdc 25%,#b4b4b8 60%,#6f6f78 100%)"></div>
  <h2 class="serif abs" style="left:88px;top:2580px;font-size:34px">Book an appointment</h2>
  <div class="form-box">
    <div style="display:grid;grid-template-columns:1fr 1fr;gap:30px 8px">
      <div class="field"><label>First name</label><div>Enter name</div></div>
      <div class="field"><label>Last name</label><div>Enter name</div></div>
      <div class="field"><label>Phone</label><div>Enter number</div></div>
      <div class="field"><label>Email</label><div>Enter email</div></div>
    </div>
    <div class="field" style="margin-top:30px"><label>Message</label><div style="height:86px">Type message</div></div>
    <div style="margin-top:34px;height:42px;background:#fff;border-radius:3px;display:flex;align-items:center;justify-content:center;font-size:11px;font-weight:700;color:#222;text-transform:uppercase">Book now</div>
  </div>
</section>

<section>
  <h2 class="section-title serif" style="top:3160px">Patient Education Center</h2>
  <div class="edu" style="left:143px">
    <div class="edu-circle" style="background:var(--blue)">
      <svg width="76" height="70" viewBox="0 0 76 70" fill="none" stroke="#fff" stroke-width="3"><rect x="20" y="4" width="36" height="20"/><rect x="4" y="22" width="68" height="30" rx="4"/><rect x="18" y="40" width="40" height="26" fill="#2a78b3"/><path d="M26 50h24M26 58h24"/></svg>
    </div>
    <b>Print</b><small>Patient forms</small>
  </div>
  <div class="edu-divider" style="left:447px"></div>
  <div class="edu" style="left:451px">
    <div class="edu-circle" style="background:var(--red)">
      <svg width="76" height="66" viewBox="0 0 76 66" fill="none" stroke="#fff" stroke-width="3"><rect x="6" y="4" width="64" height="44" rx="3"/><path d="M31 16l14 10-14 10z"/><path d="M6 58h64"/><circle cx="26" cy="58" r="4" fill="#d5364f"/></svg>
    </div>
    <b>Watch</b><small>Educational videos</small>
  </div>
  <div class="edu-divider" style="left:755px"></div>
  <div class="edu" style="left:759px">
    <div class="edu-circle" style="background:#333">
      <svg width="76" height="64" viewBox="0 0 76 64" fill="none" stroke="#fff" stroke-width="3"><rect x="4" y="4" width="68" height="56" rx="3"/><path d="M4 14h68"/><rect x="12" y="22" width="20" height="16"/><path d="M38 24h26M38 32h26M12 46h52M12 52h52"/></svg>
    </div>
    <b>Visit</b><small>Patient portal</small>
  </div>
</section>

<section>
  <h2 class="section-title serif" style="top:3573px">Our Satisfied Patients</h2>
  <div class="review" style="left:90px">
    <div class="quote">“</div>
    <p>Wonderful people, have been using the firm now for over 20 years.Would recommend to everyone. A family firm you can trust. Very efficient.</p>
    <div class="reviewer"><div class="avatar"></div><div><b>— Marlo Prentiss</b><small>a year ago</small></div></div>
    <div class="stars">★★★★★</div>
  </div>
  <div class="review" style="left:553px">
    <div class="quote">“</div>
    <p>I have been with Tobin and his team for many years now. I couldn't recommend them highly enough. Great accountants to deal with.</p>
    <div class="reviewer"><div class="avatar"></div><div><b>— Dena Quorvik</b><small>a year ago</small></div></div>
    <div class="stars">★★★★★</div>
  </div>
  <div class="review" style="left:1016px">
    <div class="quote">“</div>
    <p>We have had the best possible service, he speaks clearly and is always</p>
    <div class="reviewer"><div class="avatar"></div></div>
  </div>
  <div class="abs" style="left:583px;top:3912px;display:flex;gap:6px">
    <i style="width:7px;height:7px;border-radius:50%;background:#ccc"></i><i style="width:7px;height:7px;border-radius:50%;background:#333"></i><i style="width:7px;height:7px;border-radius:50%;background:#ccc"></i>
  </div>
</section>

<section>
  <h2 class="section-title serif" style="top:3984px">Blogs From Your Health</h2>
  <div class="ph" role="img" aria-label="Older man holding his lower back while a woman supports him" style="left:94px;top:4073px;width:568px;height:412px;border-radius:3px;background:linear-gradient(140deg,#eeeeee 0%,#cfd3d6 50%,#8f9aa3 100%)"></div>
  <div class="abs" style="left:94px;top:4505px;width:560px">
    <div class="blog-date">28 July 2023</div>
    <div class="blog-title" style="margin-top:8px">Coastline Magazine top doctors for the 4th year in a row!</div>
    <div class="read-more" style="margin-top:6px">Read more</div>
  </div>
  <div class="small-post" role="img" aria-label="Therapist massaging a patient's back" style="top:4073px;background:linear-gradient(140deg,#e4e4e4,#b7a69b)"></div>
  <div class="small-meta" style="top:4115px"><div class="blog-date">28 July 2023</div><div class="blog-title" style="margin-top:10px">How we can fix any problem in tailbone in back.</div><div class="read-more" style="margin-top:4px">Read more</div></div>
  <div class="small-post" role="img" aria-label="Therapist stretching a patient's arm" style="top:4255px;background:linear-gradient(140deg,#e9ecef,#7f94a8)"></div>
  <div class="small-meta" style="top:4297px"><div class="blog-date">28 July 2023</div><div class="blog-title" style="margin-top:10px">How we can cover injury pain by exercise</div><div class="read-more" style="margin-top:4px">Read more</div></div>
  <div class="small-post" role="img" aria-label="Patient receiving sound therapy" style="top:4437px;background:linear-gradient(140deg,#eef0f2,#8fa7bd)"></div>
  <div class="small-meta" style="top:4479px"><div class="blog-date">28 July 2023</div><div class="blog-title" style="margin-top:10px">Relax &amp; de-stress with sound therapy</div><div class="read-more" style="margin-top:4px">Read more</div></div>
  <div class="btn btn-blue abs" style="left:533px;top:4640px;width:134px;height:36px">View all blog</div>
</section>

<footer class="footer">
  <div class="logo" style="top:223px">
    <div class="logo-name" style="font-size:50px">KESTRA</div>
    <div class="logo-sub" style="font-size:12px">KESTRA ORTHOPEDIC</div>
  </div>
  <div class="abs" style="left:137px;top:322px"><span class="social"></span><span class="social"></span><span class="social"></span></div>

  <div class="foot-title" style="left:379px;top:167px">Quick links</div>
  <div class="foot-list" style="left:379px;top:214px">About Us<br>Services<br>Our Doctors<br>Conditions &amp; Treatment<br>Patient Info<br>Blog<br>Contact Us</div>

  <div class="foot-title" style="left:603px;top:167px">Contact us</div>
  <div class="foot-list" style="left:603px;top:214px;line-height:18px">
    <div style="display:flex;gap:10px"><svg width="12" height="12" viewBox="0 0 24 24"><path fill="#4a9be0" d="M6.6 10.8a15 15 0 006.6 6.6l2.2-2.2c.3-.3.7-.4 1-.2 1.1.4 2.3.6 3.6.6.6 0 1 .4 1 1V20c0 .6-.4 1-1 1A17 17 0 013 4c0-.6.4-1 1-1h3.5c.6 0 1 .4 1 1 0 1.3.2 2.5.6 3.6z"/></svg><span>Phone<br>(555) 318-2290</span></div>
    <div style="display:flex;gap:10px;margin-top:14px"><svg width="12" height="12" viewBox="0 0 24 24"><path fill="#4a9be0" d="M2 5h20v14H2zm2 2v.5l8 5 8-5V7z"/></svg><span>Email<br>care@kestraortho.com</span></div>
    <div style="display:flex;gap:10px;margin-top:14px"><svg width="12" height="12" viewBox="0 0 24 24"><path fill="#4a9be0" d="M12 2a7 7 0 00-7 7c0 5 7 13 7 13s7-8 7-13a7 7 0 00-7-7zm0 9.5a2.5 2.5 0 110-5 2.5 2.5 0 010 5z"/></svg><span>Location<br>210 Alder Lane, California<br>95946 United States</span></div>
  </div>

  <div class="foot-title" style="left:842px;top:167px">Join our newsletter</div>
  <div class="foot-list" style="left:842px;top:214px;line-height:18px;width:230px">Will send you weekly updates for your better experience...</div>
  <div class="abs" style="left:842px;top:271px;width:270px;height:44px;background:#4a4a4a;border-radius:3px;display:flex;align-items:center;padding:0 14px;gap:8px;font-size:12px;color:#ddd">
    <svg width="12" height="10" viewBox="0 0 24 20"><path fill="#bbb" d="M1 1h22v18H1zm2 2v.5l9 6 9-6V3z"/></svg>
    <span style="flex:1">Enter email address</span>
    <svg width="14" height="14" viewBox="0 0 24 24"><path fill="#fff" d="M2 11L22 2l-9 20-2-8z"/></svg>
  </div>

  <div class="abs" style="left:88px;top:442px;width:1024px;height:1px;background:#555"></div>
  <div class="abs" style="left:0;width:1200px;top:476px;text-align:center;font-size:11px;font-weight:500;color:#fff">COPYRIGHT © 2023 KESTRA ORTHOPEDIC - ALL RIGHTS RESERVED</div>
  <div class="abs" style="left:1130px;top:458px;width:46px;height:46px;border-radius:50%;background:var(--red);display:flex;align-items:center;justify-content:center">
    <svg width="22" height="20" viewBox="0 0 24 22"><path fill="#fff" d="M12 1C6 1 1 5 1 10c0 2.5 1.2 4.7 3.2 6.3L3 21l5-2.6c1.2.4 2.6.6 4 .6 6 0 11-4 11-9S18 1 12 1z"/><circle cx="7.5" cy="10" r="1.4" fill="#d5364f"/><circle cx="12" cy="10" r="1.4" fill="#d5364f"/><circle cx="16.5" cy="10" r="1.4" fill="#d5364f"/></svg>
  </div>
</footer>

<section class="cta">
  <div class="serif abs" style="left:78px;top:52px;color:#fff;font-size:32px">Ready to start?</div>
  <div class="serif abs" style="left:78px;top:98px;color:#fff;font-size:22px">Request an appointment today</div>
  <div class="abs" style="left:617px;top:72px;width:174px;height:48px;background:#fff;border-radius:3px;display:flex;align-items:center;justify-content:center;font-size:12px;font-weight:600;color:#222;text-transform:uppercase">Appointment</div>
</section>

</body>
</html>
```